Business Card Design Project

We need business cards for our new business, Veltrano Skyworks. We specialize in aerial videography and photography via drone. Currently we are mainly focusing on real estate videography but will branch into other markets and may even host training classes for flying drones.
Cards should include:
Name
Phone Number
Email Address
Web address
We will need to customize for more than one person and would like those fields to be editable
eps file logos are uploaded now, thanks!
Target Market(s)
Real Estate Agents, hotels, rental agencies and people who have recently purchase drones
Industry/Entity Type
Videography

```html
<!DOCTYPE html>
<html lang="en">
<head>
<meta charset="utf-8">
<title>Veltrano Skyworks – Business Card</title>
<link rel="stylesheet" href="https://fonts.googleapis.com/css2?family=Arimo:wght@400&family=Michroma&display=swap">
<style>
  :root {
    --page-bg: #e9e6e1;
    --card-dark-center: #4a4a4c;
    --card-dark-edge: #111112;
    --card-light: #ffffff;
    --brand-orange: #f3a312;
    --ink: #2b2b2b;
    --ink-soft: #3a3a3a;
    --on-dark: #d9d9d9;
  }
  * { margin: 0; padding: 0; box-sizing: border-box; }
  html, body {
    width: 1200px; height: 533px; overflow: hidden;
    background: var(--page-bg);
  }
  .canvas { position: relative; width: 1200px; height: 533px; }

  .card-back, .card-front {
    position: absolute; top: 127px; height: 279px;
    box-shadow: 0 2px 6px rgba(0,0,0,.25);
  }
  .card-back {
    left: 120px; width: 479px;
    background: radial-gradient(ellipse at 50% 42%, var(--card-dark-center) 0%, var(--card-dark-edge) 78%);
    display: flex; flex-direction: column; align-items: center; justify-content: center; gap: 14px;
  }
  .card-back .brand-mark {
    width: 102px; height: 102px; background: var(--brand-orange);
  }
  .card-back .brand-name {
    font-family: "Michroma", sans-serif; font-size: 13px; letter-spacing: 2px;
    color: var(--on-dark);
  }

  .card-front {
    left: 599px; width: 480px; background: var(--card-light);
  }
  .brand-lockup {
    position: absolute; left: 41px; top: 43px;
    display: flex; align-items: center; gap: 10px;
  }
  .brand-lockup .brand-mark { width: 58px; height: 58px; background: var(--brand-orange); }
  .brand-lockup .brand-name {
    font-family: "Michroma", sans-serif; font-size: 18px; letter-spacing: 1px;
    color: var(--ink);
  }

  .person-name {
    position: absolute; left: 112px; top: 166px;
    font-family: "Michroma", sans-serif; font-size: 14px; letter-spacing: 1px;
    color: var(--ink);
  }
  .address {
    position: absolute; left: 111px; top: 210px;
    font-family: "Arimo", sans-serif; font-size: 11px; line-height: 13.6px;
    color: var(--ink-soft); font-style: normal;
  }
  .contacts {
    position: absolute; left: 306px; top: 224px; list-style: none;
    font-family: "Arimo", sans-serif; font-size: 11px; line-height: 13.6px;
    color: var(--ink-soft);
  }
  .contacts li { display: flex; align-items: center; gap: 4px; }
  .contacts .icon { width: 6px; height: 6px; }
</style>
</head>
<body>
<main class="canvas">
  <section class="card-back" aria-label="Card back">
    <div class="brand-mark"></div>
    <div class="brand-name">VELTRANO SKYWORKS</div>
  </section>

  <section class="card-front" aria-label="Card front">
    <div class="brand-lockup">
      <div class="brand-mark"></div>
      <div class="brand-name">VELTRANO SKYWORKS</div>
    </div>

    <h1 class="person-name">RAVI TANDEL</h1>

    <address class="address">
      214, Lakeview Crest,<br>
      2nd Cross, 6th Main,<br>
      Hill Colony, Park Layout,<br>
      Sundarpet, Bangalore-560 042
    </address>

    <ul class="contacts">
      <li>
        <svg class="icon" viewBox="0 0 6 6" aria-hidden="true"><rect x="1.5" y="0" width="3" height="6" rx="0.6" fill="#f3a312"/></svg>
        98450 612 78
      </li>
      <li>
        <svg class="icon" viewBox="0 0 6 6" aria-hidden="true"><rect x="0.4" y="1" width="5.2" height="4" fill="none" stroke="#f3a312" stroke-width="0.9"/></svg>
        info@veltrano.com
      </li>
      <li>
        <svg class="icon" viewBox="0 0 6 6" aria-hidden="true"><rect x="0.4" y="0.4" width="5.2" height="5.2" fill="none" stroke="#f3a312" stroke-width="0.9"/></svg>
        veltrano.com
      </li>
    </ul>
  </section>
</main>
</body>
</html>
```